MS Word and MS Powerpoint template creation using existing logo as style guide

Create a professional looking MS Word document template and MS powerpoint template for Korvath Advisory Pty Ltd using a logo that's already been created as the style guide. Korvath is a professional services business providing strategy, governance and execution support to small and medium business, Boards and executive teams. refer design brief.

Target Market(s)

Small to medium business, Chairs, Boards, executive teams, general managers

Industry/Entity Type

Professional business services, consultancy, business support outsourcing

Font styles to use
Other font styles liked:
• calibri

Requirements
Must have
• leverage the existing logo for colour scheme. Use the KORVATH logo type font. Fully editable templates Word and MS Powerpoint,
Nice to have
• Refer to the design brief
Should not have
• animations, cartoons, stock images of people.

```html
<!DOCTYPE html>
<html lang="en">
<head>
<meta charset="utf-8">
<title>Korvath Slide Templates</title>
<link href="https://fonts.googleapis.com/css2?family=Poppins:wght@400;500;600;700;800&display=swap" rel="stylesheet">
<style>
:root{
  --navy:#062d44;
  --black:#1d1d1d;
  --green:#3b9b4a;
  --page:#e3e4e6;
  --card:#f1f1f1;
  --ink:#1f2a30;
  --white:#ffffff;
}
*{margin:0;padding:0;box-sizing:border-box}
html,body{width:841px;height:1200px;overflow:hidden}
body{background:var(--page);font-family:"Poppins",sans-serif;color:var(--ink);position:relative}
.sheet-title{position:absolute;top:32px;left:0;width:841px;text-align:center;font-weight:700;font-size:21px;color:var(--navy);letter-spacing:.3px}
.slide{position:absolute;width:322px;height:181px;background:var(--white);overflow:hidden}
.slide.dark{background:var(--navy);color:var(--white)}
.col-l{left:84px}.col-r{left:435px}
.row1{top:90px}.row2{top:299px}.row3{top:508px}.row4{top:718px}.row5{top:928px}
.abs{position:absolute}
.base-bar{position:absolute;left:0;bottom:0;width:100%;height:4px;background:var(--navy)}
.footer-mark{position:absolute;right:12px;bottom:7px;font-size:5.6px;letter-spacing:.5px;font-weight:700;color:var(--navy)}
.dark .footer-mark{color:var(--white)}
.h-slide{font-weight:700;font-size:14.5px;line-height:13.5px;color:var(--navy);text-transform:uppercase}
.dark .h-slide{color:var(--white)}
.center{text-align:center;left:0;width:100%}
.body-s{font-size:5.2px;line-height:6.6px}
.lorem{font-size:4.25px;line-height:6.1px;text-align:justify}
.photo-wash{position:absolute;inset:0;background:linear-gradient(100deg,#ffffff 20%,#ececec 50%,#f4f4f4 75%,#ffffff 100%)}
.brand{font-weight:700;color:var(--navy);letter-spacing:.3px;font-size:15px;line-height:16px}
.icon-tile{position:absolute;top:105px;width:37px;height:36px;background:#efefef}
.icon-label{position:absolute;top:144px;width:60px;text-align:center;font-size:5.2px;font-weight:600;color:var(--ink)}
.why-card{position:absolute;top:59px;width:74px;height:87px;background:var(--card);text-align:center}
.why-icon{position:absolute;top:9px;left:26px;width:22px;height:22px;background:var(--navy)}
.why-title{position:absolute;top:43px;left:0;width:100%;font-size:4.4px;font-weight:700;line-height:5px;color:var(--navy)}
.why-text{position:absolute;top:57px;left:9px;width:56px;font-size:3.3px;line-height:3.9px;color:var(--ink)}
.offer{position:absolute;width:95px}
.offer svg{display:block;width:12px;height:12px}
.offer-title{font-size:5.4px;font-weight:700;color:var(--navy);margin-top:2px}
.offer-text{font-size:3.3px;line-height:4px;margin-top:1px}
.sub-col{position:absolute;top:50px;width:80px;text-align:center}
.sub-col h3{font-size:6.6px;font-weight:700;margin-bottom:5px}
.sub-col p{font-size:4.2px;line-height:5.7px;text-align:justify;text-align-last:center}
.divider{position:absolute;top:48px;height:92px;border-left:.6px dashed rgba(255,255,255,.55)}
.art{position:absolute;border-radius:4px}
</style>
</head>
<body>

<h1 class="sheet-title">DEMI TEXT</h1>

<!-- Cover, left aligned -->
<section class="slide col-l row1">
  <div class="photo-wash" role="img" aria-label="Faded photograph of a padlock resting on a measuring caliper"></div>
  <svg class="abs" style="left:0;top:0" width="322" height="181" viewBox="0 0 322 181">
    <polygon points="233,0 270,0 322,32 322,62" fill="var(--navy)"/>
    <polygon points="232,42 264,42 322,80 322,104" fill="var(--black)"/>
  </svg>
  <div class="abs brand" style="left:19px;top:18px">Korvath</div>
  <h2 class="abs" style="left:18px;top:94px;width:210px;font-size:12.2px;line-height:13.8px;font-weight:700;color:var(--navy)">Precision Crafted Cybersecurity For An Increasingly Complex AI Driven World</h2>
  <div class="abs" style="left:18px;top:139px;width:66px;height:.6px;background:var(--green)"></div>
  <p class="abs" style="left:18px;top:142px;font-size:6.2px;color:var(--ink)">When Trust, Discretion and Deep Expertise are Non-Negotiable</p>
  <p class="abs" style="left:18px;top:163px;font-size:4.8px;color:var(--ink)">www.KORVATH.com</p>
</section>

<!-- Cover, centred -->
<section class="slide col-r row1">
  <div class="photo-wash" role="img" aria-label="Faded photograph of a padlock resting on a measuring caliper"></div>
  <svg class="abs" style="left:0;top:0" width="322" height="181" viewBox="0 0 322 181">
    <polygon points="0,0 64,0 161,68 161,111" fill="var(--navy)"/>
    <polygon points="161,68 256,0 322,0 161,111" fill="var(--black)"/>
  </svg>
  <div class="abs center brand" style="top:16px;font-size:11px;line-height:12px">Korvath</div>
  <h2 class="abs center h-slide" style="top:121px;font-size:12.4px;line-height:12.2px">Precision Crafted Cybersecurity<br>For An Increasingly Complex<br>AL Driven World</h2>
  <p class="abs center" style="top:160px;font-size:6.2px">When Trust, Discretion and Deep Expertise are Non-Negotiable</p>
</section>

<!-- Sustainable cyber security -->
<section class="slide col-l row2">
  <h2 class="abs center h-slide" style="top:16px">Sustainable<br>Cyber Security</h2>
  <p class="abs center body-s" style="top:49px;font-size:4.8px;line-height:6.4px">Shieldmere Delivers Best Of Breed, Boutique Information Security<br>Services That Protect, Empower And Delight Our Customers.</p>
  <h3 class="abs center" style="top:85px;font-size:7.6px;font-weight:600;color:var(--navy)">CYBER SECURITY SERVICES FOR</h3>
  <div class="icon-tile" style="left:45px" role="img" aria-label="Energy icon"></div>
  <div class="icon-tile" style="left:110px" role="img" aria-label="Utilities icon"></div>
  <div class="icon-tile" style="left:174px" role="img" aria-label="Manufacturing icon"></div>
  <div class="icon-tile" style="left:239px" role="img" aria-label="Technology icon"></div>
  <span class="icon-label" style="left:33px">Energy</span>
  <span class="icon-label" style="left:98px">Utilities</span>
  <span class="icon-label" style="left:162px">Manufacturing</span>
  <span class="icon-label" style="left:227px">Technology</span>
  <span class="footer-mark">KORVATH</span>
  <div class="base-bar"></div>
</section>

<!-- Why choose us -->
<section class="slide col-r row2">
  <h2 class="abs center h-slide" style="top:16px">Why Choose Us</h2>
  <p class="abs center body-s" style="top:33px;font-size:4.8px;line-height:6.4px">We are not just any security consultancy. We are passionate about your success.<br>We deliver YOUR needs. We are Shieldmere.</p>
  <div class="why-card" style="left:37px">
    <div class="why-icon"><svg width="22" height="22" viewBox="0 0 22 22"><path d="M10.4 6c-2.6-1-5 1-4.6 3.4-1.6 1-1.4 3.6.4 4.3 0 2 2.2 3 4.2 2.2z M11.6 6c2.6-1 5 1 4.6 3.4 1.6 1 1.4 3.6-.4 4.3 0 2-2.2 3-4.2 2.2z" fill="#fff"/></svg></div>
    <div class="why-title">DEEP<br>EXPERTISE</div>
    <p class="why-text">Our people have decades of experience protecting the largest organisations in the world using best of breed process and technology.</p>
  </div>
  <div class="why-card" style="left:124px">
    <div class="why-icon"><svg width="22" height="22" viewBox="0 0 22 22"><path d="M7 5h8v4a4 4 0 0 1-8 0z M5 6h2v2.5a2 2 0 0 1-2-2z M17 6h-2v2.5a2 2 0 0 0 2-2z M10 12.5h2v3h-2z M8 15.5h6v1.6H8z" fill="#fff"/></svg></div>
    <div class="why-title">OUTCOME<br>FOCUSED</div>
    <p class="why-text">Our passion is your success. We prioritise your needs over rigid process so that you get the results your organisation needs.</p>
  </div>
  <div class="why-card" style="left:211px">
    <div class="why-icon"><svg width="22" height="22" viewBox="0 0 22 22"><path d="M11 16.5 5.6 11a3.2 3.2 0 0 1 5.4-3.6A3.2 3.2 0 0 1 16.4 11z" fill="none" stroke="#fff" stroke-width="1.2"/></svg></div>
    <div class="why-title">PURPOSE<br>DRIVEN</div>
    <p class="why-text">Keeping your organisation secure means we further support our mission to deliver a more equal, secure and sustainable world.</p>
  </div>
  <span class="footer-mark">KORVATH</span>
  <div class="base-bar"></div>
</section>

<!-- Advanced provider -->
<section class="slide dark col-l row3">
  <div class="art" style="left:25px;top:50px;width:100px;height:88px;background:radial-gradient(circle at 50% 50%,#3b9b4a55,#062d44 72%)" role="img" aria-label="Illustration of a laptop with security gauge, gears and coins"></div>
  <h2 class="abs h-slide" style="left:135px;top:43px">Advanced Cyber<br>Security Provider</h2>
  <p class="abs body-s" style="left:135px;top:83px;width:162px">We are partnered with some of the worlds best known technology organisations such as Veltrane, Clearbond and Simulix and deliver leading-edge information security to meet your organisation’s needs.</p>
  <p class="abs body-s" style="left:135px;top:116px;width:162px">Our global experience within utilities, banking, technology, commodities and financial markets comes from having worked with leading global organisations in these sectors.</p>
  <span class="footer-mark">KORVATH</span>
</section>

<!-- Sustainable services -->
<section class="slide col-r row3">
  <h2 class="abs h-slide" style="left:19px;top:17px">Sustainable<br>Security Services</h2>
  <p class="abs body-s" style="left:19px;top:54px;width:158px">We want everyone to benefit from the opportunities that technology has to offer. A foundation to this is supporting our customers in ensuring their services are secure.</p>
  <p class="abs body-s" style="left:19px;top:80px;width:158px">We promote equality and diversity so that all can benefit, and have devoted time and resources to supporting developing economies. We have adopted the UN sustainable development goals, and support others in following our footsteps.</p>
  <p class="abs body-s" style="left:19px;top:118px;width:158px">We will continue to explore new ways to support and give back to society and the world.</p>
  <div class="art" style="left:195px;top:24px;width:110px;height:112px;background:linear-gradient(160deg,#e6f2e8,#cfe6d3)" role="img" aria-label="Illustration of a certification checklist with a magnifying glass"></div>
  <span class="footer-mark">KORVATH</span>
  <div class="base-bar"></div>
</section>

<!-- What we offer -->
<section class="slide col-l row4">
  <h2 class="abs center h-slide" style="top:17px">What We Offer</h2>
  <div class="offer" style="left:15px;top:45px">
    <svg viewBox="0 0 12 12"><path d="M6 .8 7.5 4.2 11.2 4.5 8.4 7 9.2 10.7 6 8.8 2.8 10.7 3.6 7 .8 4.5 4.5 4.2z" fill="none" stroke="var(--green)" stroke-width=".6"/></svg>
    <div class="offer-title">SECURITY STRATEGY</div>
    <p class="offer-text">We can help you see the bigger picture and prioritise your information security efforts, as well as design and implement new systems, structures and operating models to deliver a safer and more compliant service.</p>
  </div>
  <div class="offer" style="left:123px;top:45px">
    <svg viewBox="0 0 12 12"><path d="M6 .8 7.5 4.2 11.2 4.5 8.4 7 9.2 10.7 6 8.8 2.8 10.7 3.6 7 .8 4.5 4.5 4.2z" fill="none" stroke="var(--green)" stroke-width=".6"/></svg>
    <div class="offer-title">DETECTION AND RESPONSE</div>
    <p class="offer-text">We have decades of experience delivering operational security. Our team and partners have the tools and processes to take the headaches out of day to day operations.</p>
  </div>
  <div class="offer" style="left:227px;top:45px">
    <svg viewBox="0 0 12 12"><path d="M6 .8 7.5 4.2 11.2 4.5 8.4 7 9.2 10.7 6 8.8 2.8 10.7 3.6 7 .8 4.5 4.5 4.2z" fill="none" stroke="var(--green)" stroke-width=".6"/></svg>
    <div class="offer-title">GRC ADVISORY</div>
    <p class="offer-text">Your organisation needs to meet certain standards and regulations. We understand these intimately and can help plan &amp; transform your services to a compliant state.</p>
  </div>
  <div class="offer" style="left:15px;top:103px">
    <svg viewBox="0 0 12 12"><path d="M6 .8 7.5 4.2 11.2 4.5 8.4 7 9.2 10.7 6 8.8 2.8 10.7 3.6 7 .8 4.5 4.5 4.2z" fill="none" stroke="var(--green)" stroke-width=".6"/></svg>
    <div class="offer-title">SECURITY TRANSFORMATION</div>
    <p class="offer-text">Either as part of a broader technology transformation or discrete programme, we help design and implement transformations to reduce risk, improve costs and deliver a functional and compliant state.</p>
  </div>
  <div class="offer" style="left:123px;top:103px">
    <svg viewBox="0 0 12 12"><path d="M6 .8 7.5 4.2 11.2 4.5 8.4 7 9.2 10.7 6 8.8 2.8 10.7 3.6 7 .8 4.5 4.5 4.2z" fill="none" stroke="var(--green)" stroke-width=".6"/></svg>
    <div class="offer-title">SECURITY TRAINING</div>
    <p class="offer-text">Your people are your biggest risk. We help mitigate this with structured training and awareness programmes that ensure an improved level of security understanding across your organisation.</p>
  </div>
  <div class="offer" style="left:227px;top:103px">
    <svg viewBox="0 0 12 12"><path d="M6 .8 7.5 4.2 11.2 4.5 8.4 7 9.2 10.7 6 8.8 2.8 10.7 3.6 7 .8 4.5 4.5 4.2z" fill="none" stroke="var(--green)" stroke-width=".6"/></svg>
    <div class="offer-title">CLOUD SECURITY</div>
    <p class="offer-text">We support customers with new and existing migrations to cloud providers. We ensure it is treated as part of the overall strategy and not an isolated component.</p>
  </div>
  <span class="footer-mark">KORVATH</span>
  <div class="base-bar"></div>
</section>

<!-- Two column text -->
<section class="slide col-r row4">
  <h2 class="abs h-slide" style="left:18px;top:17px">Heading Goes Here</h2>
  <p class="abs lorem" style="left:18px;top:43px;width:139px">Lorem ipsum dolor sit amet, consectetuer adipiscing elit, sed diam nonummy nibh euismod tincidunt ut laoreet dolore magna aliquam erat volutpat. Ut wisi enim ad minim veniam, quis nostrud exerci tation ullamcorper suscipit lobortis nisl ut aliquip ex ea commodo consequat. Duis autem vel eum iriure dolor in hendrerit in vulputate velit esse molestie consequat, vel illum dolore eu feugiat nulla facilisis at vero eros et accumsan et facilisi.</p>
  <p class="abs lorem" style="left:18px;top:103px;width:139px">Lorem ipsum dolor sit amet, cons ectetuer adipiscing elit, sed diam nonummy nibh euismod tincidunt ut laoreet dolore magna aliquam erat volutpat. Ut wisi enim ad minim veniam, quis nostrud exerci tation ullamcorper suscipit lobortis nisl ut aliquip ex ea commodo consequat.</p>
  <p class="abs lorem" style="left:167px;top:43px;width:139px">Lorem ipsum dolor sit amet, consectetuer adipiscing elit, sed diam nonummy nibh euismod tincidunt ut laoreet dolore magna aliquam erat volutpat. Ut wisi enim ad minim veniam, quis nostrud exerci tation ullamcorper suscipit lobortis nisl ut aliquip ex ea commodo consequat. Duis autem vel eum iriure dolor in hendrerit in vulputate velit esse molestie consequat, vel illum dolore eu feugiat nulla facilisis at vero eros et accumsan et facilisi.</p>
  <p class="abs lorem" style="left:167px;top:103px;width:139px">Lorem ipsum dolor sit amet, cons ectetuer adipiscing elit, sed diam nonummy nibh euismod tincidunt ut laoreet dolore magna aliquam erat volutpat. Ut wisi enim ad minim veniam, quis nostrud exerci tation ullamcorper suscipit lobortis nisl ut aliquip ex ea commodo consequat.</p>
  <span class="footer-mark">KORVATH</span>
  <div class="base-bar"></div>
</section>

<!-- Single column text -->
<section class="slide col-l row5">
  <h2 class="abs h-slide" style="left:17px;top:17px">Heading Goes Here</h2>
  <p class="abs lorem" style="left:17px;top:43px;width:288px;text-align:left">Lorem ipsum dolor sit amet, consectetuer adipiscing elit, sed diam nonummy nibh euismod tincidunt ut laoreet dolore magna aliquam erat volutpat. Ut wisi enim ad minim veniam, quis nostrud exerci tation ullamcorper suscipit lobortis nisl ut aliquip ex ea commodo consequat. Duis autem vel eum iriure dolor in hendrerit in vulputate velit esse molestie consequat, vel illum dolore eu feugiat nulla facilisis at vero eros et accumsan et facilisi.</p>
  <p class="abs lorem" style="left:17px;top:77px;width:288px;text-align:left">Lorem ipsum dolor sit amet, cons ectetuer adipiscing elit, sed diam nonummy nibh euismod tincidunt ut laoreet dolore magna aliquam erat volutpat. Ut wisi enim ad minim veniam, quis nostrud exerci tation ullamcorper suscipit lobortis nisl ut aliquip ex ea commodo consequat Lorem ipsum dolor sit amet, consectetuer adipiscing elit, sed diam nonummy nibh euismod tincidunt ut laoreet dolore magna aliquam erat volutpat. Ut wisi enim ad minim veniam, quis nostrud exerci tation ullamcorper suscipit lobortis nisl ut aliquip ex ea commodo consequat. Duis autem vel eum iriure dolor in hendrerit in vulputate velit esse molestie consequat, vel illum dolore eu feugiat nulla facilisis at vero eros et accumsan et facilisi.</p>
  <p class="abs lorem" style="left:17px;top:125px;width:288px;text-align:left">Lorem ipsum dolor sit amet, cons ectetuer adipiscing elit, sed diam nonummy nibh euismod tincidunt ut laoreet dolore magna aliquam erat volutpat. Ut wisi enim ad minim veniam, quis nostrud exerci tation ullamcorper suscipit lobortis nisl ut aliquip ex ea commodo consequat.</p>
  <span class="footer-mark">KORVATH</span>
  <div class="base-bar"></div>
</section>

<!-- Three column dark -->
<section class="slide dark col-r row5">
  <h2 class="abs center h-slide" style="top:17px">Heading Goes Here</h2>
  <div class="sub-col" style="left:27px"><h3>SUBTITLE</h3><p>Lorem ipsum dolor sit amet, consectetuer adipiscing elit, sed diam nonummy nibh euismod tincidunt ut laoreet dolore magna aliquam erat volutpat. Ut wisi enim ad minim veniam, quis nostrud exerci tation ullamcorper suscipit lobortis nisl ut aliquip ex ea commodo consequat. Duis autem vel eum iriure dolor in hendrerit in vulputate velit esse molestie consequat, vel illum dolore eu feugiat nulla facilisis at vero eros et accumsan et facilisi.</p></div>
  <div class="divider" style="left:114px"></div>
  <div class="sub-col" style="left:121px"><h3>SUBTITLE</h3><p>Lorem ipsum dolor sit amet, consectetuer adipiscing elit, sed diam nonummy nibh euismod tincidunt ut laoreet dolore magna aliquam erat volutpat. Ut wisi enim ad minim veniam, quis nostrud exerci tation ullamcorper suscipit lobortis nisl ut aliquip ex ea commodo consequat. Duis autem vel eum iriure dolor in hendrerit in vulputate velit esse molestie consequat, vel illum dolore eu feugiat nulla facilisis at vero eros et accumsan et facilisi.</p></div>
  <div class="divider" style="left:208px"></div>
  <div class="sub-col" style="left:216px"><h3>SUBTITLE</h3><p>Lorem ipsum dolor sit amet, consectetuer adipiscing elit, sed diam nonummy nibh euismod tincidunt ut laoreet dolore magna aliquam erat volutpat. Ut wisi enim ad minim veniam, quis nostrud exerci tation ullamcorper suscipit lobortis nisl ut aliquip ex ea commodo consequat. Duis autem vel eum iriure dolor in hendrerit in vulputate velit esse molestie consequat, vel illum dolore eu feugiat nulla facilisis at vero eros et accumsan et facilisi.</p></div>
  <span class="footer-mark">KORVATH</span>
</section>

</body>
</html>
```